Supplement Company Needs a Protein Powder Pouch Design

We are looking for a modern and fresh design for our 500g pouches of protein powder as our current design is not eye catching or exciting enough.

This new design will be printed on both sides of a 178mm x 280mm x 101mm pouch.

We have 4 flavours. These are Banana Ice Cream, Chocolate Deluxe, Strawberries & Cream and Vanilla Ice Cream.

Industry/Entity Type

Supplement

Requirements
Must have
• Attractive and eye catching front and space for all the nutritional information and ingredients on the back.

Must clearly state 'food supplement' somewhere on the front of the pouch.
Nice to have
• Our logo is attached.
Should not have
• No health claims as these are not allowed in the UK

```html
<!DOCTYPE html>
<html lang="en">
<head>
<meta charset="utf-8">
<title>KEEN Supplements – Protein Powder Chocolate Deluxe</title>
<link href="https://fonts.googleapis.com/css2?family=Montserrat:wght@500;700;800&family=Arimo:ital,wght@0,400;0,700;1,400&display=swap" rel="stylesheet">
<style>
  :root {
    --backdrop: #d0c8a8;
    --kraft: #b09468;
    --kraft-dark: #9c8056;
    --panel: #46474b;
    --gold: #ebd192;
    --ink: #2f2f33;
    --fine: #e4dccb;
  }
  * { box-sizing: border-box; margin: 0; padding: 0; }
  html, body { width: 1200px; height: 1200px; overflow: hidden; }
  body { background: var(--backdrop); position: relative; font-family: "Arimo", Arial, sans-serif; }

  .pouch-artwork {
    position: absolute; left: 340px; top: 205px; width: 520px; height: 790px;
    background: var(--kraft); display: flex;
  }
  .kraft-side {
    width: 70px; height: 100%;
    background: linear-gradient(180deg, var(--kraft) 0%, var(--kraft-dark) 50%, var(--kraft) 100%);
  }
  .front-panel {
    flex: 1; background: var(--panel); position: relative;
    display: flex; flex-direction: column; align-items: center;
    padding: 150px 14px 0;
    color: var(--fine);
  }
  .brand-name {
    font-family: "Montserrat", sans-serif; font-weight: 800; font-size: 30px;
    color: #fff; letter-spacing: 1px; line-height: 1;
  }
  .brand-sub {
    font-family: "Montserrat", sans-serif; font-weight: 700; font-size: 7px;
    color: #fff; letter-spacing: 4px; margin-top: 3px;
  }
  .food-supplement {
    font-family: "Montserrat", sans-serif; font-weight: 700; font-size: 12px;
    color: var(--gold); letter-spacing: 1px; margin-top: 8px;
  }
  .product-title {
    font-family: "Montserrat", sans-serif; font-weight: 800; font-size: 56px;
    color: var(--gold); letter-spacing: 4px; line-height: 1; text-align: center;
    margin-top: 8px;
  }
  .flavour-tag {
    background: var(--gold); color: var(--ink);
    font-family: "Montserrat", sans-serif; font-weight: 700; font-size: 17px;
    padding: 2px 6px; margin-top: 6px; letter-spacing: .3px;
  }
  .flavour-visual {
    width: 220px; height: 100px; margin-top: 14px; border-radius: 12px;
    background: radial-gradient(ellipse at 40% 55%, #6b3b24 0%, #5a3220 40%, rgba(70,71,75,0) 75%);
  }
  .info { width: 100%; margin-top: 8px; font-size: 7.2px; line-height: 1.3; }
  .info p { margin-bottom: 3px; }
  .label-tag { background: var(--gold); color: var(--ink); font-weight: 700; padding: 0 2px; }
  .info em { font-style: italic; }
  .nutrition {
    width: 100%; border-collapse: collapse; margin: 4px 0 6px; font-size: 5.5px;
  }
  .nutrition td { border: 0.5px solid #8a8478; padding: 1px 2px; height: 10px; }
  .nutrition .head { background: #6c6a66; }
  .nutrition .kcal { color: var(--gold); font-weight: 700; font-size: 11px; text-align: center; }
  .footer-line { display: flex; justify-content: space-between; font-size: 5.5px; font-weight: 700; margin-top: 4px; }
  .net-weight {
    margin-top: 8px; background: var(--gold); color: var(--ink);
    font-size: 8px; font-weight: 700; padding: 1px 4px;
  }
</style>
</head>
<body>
  <main class="pouch-artwork">
    <div class="kraft-side" role="img" aria-label="Kraft paper side with faint cocoa pod and leaf line illustration"></div>

    <section class="front-panel">
      <div class="brand-name">KEEN</div>
      <div class="brand-sub">SUPPLEMENTS</div>
      <div class="food-supplement">FOOD SUPLEMENT</div>
      <h1 class="product-title">PROTEIN<br>POWDER</h1>
      <div class="flavour-tag">CHOCOLATE DELUXE FLAVOUR</div>
      <div class="flavour-visual" role="img" aria-label="Chocolate pieces with a hazelnut and green leaves"></div>

      <div class="info">
        <p><span class="label-tag">SUGGESTED USE:</span> We recommend using one to two servings of 30g per day. One serving is one level scoop ( a scoop is inside this scoop ). Mix one level scoop with at least 200ml of cold water. Do not exceed recommended daily dose.</p>
        <p><span class="label-tag">STORAGE INFORMATION:</span><br><em>Store in a cool and dry place. Reseal this pouch after each use. Keep out of sight and reach of children.</em></p>

        <table class="nutrition">
          <tr class="head"><td>Nutrition facts</td><td>Per 100g</td><td>Per 30g</td><td>Per 100g</td><td>Per 30g</td><td>Per serving</td><td>Calories</td></tr>
          <tr><td>Typical values</td><td>Energy</td><td>1650kJ</td><td>Carbohydrate</td><td>4.2g</td><td>Protein</td><td rowspan="3" class="kcal">117</td></tr>
          <tr><td>per serving</td><td>Fat</td><td>6.1g</td><td>of which sugars</td><td>2.0g</td><td>Salt</td></tr>
          <tr><td>Net weight 500g</td><td>Saturates</td><td>1.9g</td><td>Fibre</td><td>1.1g</td><td>Servings</td></tr>
        </table>

        <p><span class="label-tag">INGREDIENTS:</span> Protein Blend (Soya Protein Isolate, Whey Protein Concentrate (Milk), Milk Protein (70%) Acetyl Carnitine (500mg per 100g), Flavouring, Fat Reduced Cocoa Powder (10%), Thickener (Xanthan Gum), Sweetener (Sucralose).</p>
        <p><em>Manufactured in the UK with EU protein powder (Germany) and non-EU cocoa powder (Ghana)</em></p>
        <p><span class="label-tag">CAUTION:</span> Food supplements should not be used as a substitute for a varied diet an healthy lifestyle. This product is not recommended for use by pregnant or lactating women. If you are taking any medication or are under medical supervision, you should consult with your health care professional before use, taking into consideration other supplement and medication you consume. This product is not intended for use by person under the age 16.</p>
        <div class="footer-line"><span>KEEN Supplements Limited, Mill Lane, North Barton, Devon, EX12 3QP</span><span><em>Best before: See back of pouch</em></span></div>
      </div>
      <div class="net-weight">500g</div>
    </section>

    <div class="kraft-side" role="img" aria-label="Kraft paper side with faint cocoa pod and leaf line illustration"></div>
  </main>
</body>
</html>
```